8' x 22' Enclosed work trailer

I just purchased a new work trailer and want a badass design for the exterior. Either a wrap, lettering or combo to match my truck. I have a kitchen & bathroom remodeling company - Renovo Crafters. I think it should include my logo and possibly a larger photo of a sweet kitchen and bathroom just like my old trailer. I'm attaching pics of my old trailer for reference, my existing truck, my new trailer and logo. Excited to see the results!

```html
<!DOCTYPE html>
<html lang="en">
<head>
<meta charset="utf-8">
<title>Renovo Crafters – Trailer Wrap</title>
<link href="https://fonts.googleapis.com/css2?family=Montserrat:wght@600;700&family=Playfair+Display:ital,wght@1,600&display=swap" rel="stylesheet">
<style>
  :root {
    --canvas: #e4e4e6;
    --charcoal: #3b3d42;
    --charcoal-deep: #2c2e32;
    --brand-blue: #1f6fb2;
    --sky-blue: #5fa3d8;
    --ink: #1d2533;
    --white: #ffffff;
    --photo-light: #f1f1ef;
    --photo-mid: #c9c6c0;
  }
  html, body {
    margin: 0;
    width: 833px;
    height: 1200px;
    overflow: hidden;
    background: var(--canvas);
  }
  .sheet {
    position: relative;
    width: 833px;
    height: 1200px;
  }
  .rear-panel {
    position: absolute;
    left: 136px;
    top: 150px;
    width: 560px;
    height: 400px;
  }
  .side-panel {
    position: absolute;
    left: 26px;
    top: 720px;
    width: 780px;
    height: 330px;
  }
  .brand-name {
    font-family: "Montserrat", sans-serif;
    font-weight: 700;
  }
  .tagline {
    font-family: "Playfair Display", serif;
    font-style: italic;
    font-weight: 600;
  }
  .phone, .web {
    font-family: "Montserrat", sans-serif;
    font-weight: 600;
  }
</style>
</head>
<body>
<main class="sheet">

  <!-- Rear door panel -->
  <svg class="rear-panel" viewBox="0 0 560 400" xmlns="http://www.w3.org/2000/svg">
    <defs>
      <linearGradient id="rearPhoto" x1="0" y1="0" x2="1" y2="1">
        <stop offset="0" stop-color="#8d8b88"/>
        <stop offset="0.6" stop-color="#5e5d5b"/>
        <stop offset="1" stop-color="#3f4043"/>
      </linearGradient>
    </defs>
    <path d="M30 0 H530 V30 H560 V400 H0 V30 H30 Z" fill="var(--charcoal)"/>
    <rect role="img" aria-label="Soft photo of a finished kitchen with cabinets and island" x="40" y="215" width="480" height="150" fill="url(#rearPhoto)" opacity="0.85"/>
    <path d="M0 300 C140 390 330 400 560 330 V400 H0 Z" fill="var(--brand-blue)"/>
    <path d="M0 285 C140 372 330 384 560 316 V326 C330 394 140 384 0 298 Z" fill="var(--sky-blue)"/>
    <text class="brand-name" x="280" y="120" text-anchor="middle" font-size="40" fill="var(--white)">Renovo Crafters</text>
    <text class="tagline" x="280" y="152" text-anchor="middle" font-size="18" fill="var(--white)">"Built Right, Built to Last"</text>
    <g class="phone-line" transform="translate(188 178)">
      <path d="M4 2 C2 2 1 4 2 7 C5 15 11 21 19 24 C22 25 24 24 24 22 L24 18 L19 16 L16 19 C12 17 9 14 7 10 L10 7 L8 2 Z" fill="var(--sky-blue)"/>
      <text class="phone" x="34" y="20" font-size="22" fill="var(--sky-blue)">555-014-2270</text>
    </g>
  </svg>

  <!-- Side panel -->
  <svg class="side-panel" viewBox="0 0 780 330" xmlns="http://www.w3.org/2000/svg">
    <defs>
      <linearGradient id="sidePhoto" x1="0" y1="0" x2="1" y2="0">
        <stop offset="0" stop-color="var(--photo-light)"/>
        <stop offset="0.45" stop-color="#dedcd7"/>
        <stop offset="1" stop-color="var(--photo-mid)"/>
      </linearGradient>
    </defs>
    <rect role="img" aria-label="Bright photo of a remodeled bathroom blending into a modern kitchen" x="0" y="0" width="600" height="330" fill="url(#sidePhoto)"/>
    <path d="M0 250 C200 330 410 300 545 165 L560 185 C430 325 210 340 0 300 Z" fill="var(--brand-blue)"/>
    <path d="M0 300 C210 340 430 325 560 185 L600 330 H0 Z" fill="var(--photo-light)"/>
    <path d="M0 236 C200 318 410 288 540 155 L545 165 C410 300 200 330 0 250 Z" fill="var(--sky-blue)"/>
    <path d="M560 0 C500 90 505 240 585 330 H780 V0 Z" fill="var(--charcoal)"/>
    <path d="M560 0 C500 90 505 240 585 330 H596 C518 240 512 90 572 0 Z" fill="var(--charcoal-deep)"/>
    <text class="brand-name" x="40" y="82" font-size="38" fill="var(--ink)">Renovo Crafters</text>
    <text class="tagline" x="44" y="112" font-size="17" fill="var(--ink)">"Built Right, Built to Last"</text>
    <g class="phone-line" transform="translate(44 132)">
      <path d="M4 2 C2 2 1 4 2 7 C5 15 11 21 19 24 C22 25 24 24 24 22 L24 18 L19 16 L16 19 C12 17 9 14 7 10 L10 7 L8 2 Z" fill="var(--brand-blue)"/>
      <text class="phone" x="34" y="21" font-size="23" fill="var(--brand-blue)">555-014-2270</text>
    </g>
    <text class="web" x="766" y="306" text-anchor="end" font-size="13" fill="var(--white)">www.renovo-crafters.com</text>
  </svg>

</main>
</body>
</html>
```